Driftwood Bay Private Yacht Charter "Rack Flyer"

This will be a 4" x 9" Rack flyer that is 4 colors and two sided. This is a Private Yacht charter company that is based in St Thomas, U.S. Virgin Islands. Our main product that I would like to promote on one entire side of the flyer is our Private Luxury Full Day "Gilded Galley". our charter company is unique in the fact we offer customizable itineraries and we offer unique activities that keep the family and groups engaged in fun for the entire day. We would like something with our colors.

Target Market(s)

We are trying to reach an upscale clients that are looking for a Luxury Day Charter experience. these people will be most likely staying in Private Villas or staying at the Halloway Crest or PK Bellmont.

Requirements
Must have
• Contact Information:
Ph: (340) 555-0187
email: Info@driftwoodbayvoyages.example
www.driftwoodbayvoyages.example
One side should Promote our Gilded Galley (Gilded Galley is a trademarked name).
All Guests will receive "Harbor Fizz"
> Up to 12 guests
> Full Brunch Spread to include, Assorted fruit tower, Artesian Waffle Board, Frittata's, Loaded Avocado Toast or an All American Breakfast.
> Specialty Cocktails with Bottle Service options available
List all of our Unique activities to include:
Snorkeling
Underwater WaveGlider
Cliff Diving
Paddleboarding
Towable Activities
TEXT TO BE WRITTEN:
Experience yacht charter service at its Finest!
Sail away with us on a Luxury Charter experience complete with a full brunch spread. During our sail we will take you to the hottest destination spots in the Caribbean surrounding St Thomas and St John. Warm, fresh baked afternoon cookies will be served on the way back from our days journeys. Unlimited water, sodas, beer and rum punch will be provided for the entire group to enjoy throughout the day.
_________________

On side two of the brochure you can refer to the downloaded text. We do not want pricing listed on the flyer

```html
<!DOCTYPE html>
<html lang="en">
<head>
<meta charset="utf-8">
<title>Driftwood Bay Private Yacht Charter – Rack Flyer</title>
<link href="https://fonts.googleapis.com/css2?family=Montserrat:ital,wght@0,400;0,600;0,700;0,800;1,700&display=swap" rel="stylesheet">
<style>
  :root {
    --red: #f3393c;
    --ink: #2f2f33;
    --paper: #ffffff;
    --backdrop: #e4e4e6;
    --sea-deep: #1b6f93;
    --sea-light: #5cc3d8;
    --sand: #d9c7a6;
  }
  * { box-sizing: border-box; margin: 0; padding: 0; }
  html, body { width: 1200px; height: 927px; overflow: hidden; }
  body {
    background: var(--backdrop);
    font-family: "Montserrat", Arial, sans-serif;
    color: var(--ink);
    position: relative;
  }
  .flyer {
    position: absolute;
    top: 33px;
    width: 380px;
    height: 860px;
    background: var(--paper);
    box-shadow: 0 6px 18px rgba(0,0,0,0.12);
    overflow: hidden;
  }
  .flyer--front { left: 180px; }
  .flyer--back { left: 640px; }

  /* brand */
  .brand {
    height: 96px;
    display: flex;
    align-items: center;
    justify-content: center;
    gap: 10px;
  }
  .brand__mark {
    width: 14px; height: 14px; border-radius: 50%;
    background: var(--red);
  }
  .brand__name {
    font-weight: 700;
    font-size: 26px;
    color: var(--red);
    letter-spacing: 0.5px;
  }

  .photo-hero {
    height: 200px;
    background: linear-gradient(160deg, #f4f1ea 0%, #b9d2d6 40%, #5d8d7c 70%, #3f6e86 100%);
  }

  .headline-band {
    background: var(--red);
    color: #fff;
    text-align: center;
    font-weight: 800;
    font-size: 17px;
    line-height: 1.2;
    padding: 12px 20px;
    text-transform: uppercase;
  }

  .body-copy {
    font-size: 11.2px;
    line-height: 1.42;
    text-align: justify;
    padding: 0 30px;
  }
  .body-copy p + p { margin-top: 8px; }

  .section-tab {
    display: inline-block;
    background: var(--red);
    color: #fff;
    font-weight: 700;
    font-size: 13px;
    text-transform: uppercase;
    padding: 6px 34px 6px 30px;
    clip-path: polygon(0 0, 100% 0, 88% 100%, 0 100%);
  }

  .front-content { padding-top: 14px; }
  .galley { margin-top: 14px; }
  .galley .section-tab { margin-bottom: 8px; }
  .perks {
    font-size: 11.2px;
    line-height: 1.42;
    padding: 6px 30px 0 30px;
  }
  .perks__lead { font-weight: 700; font-style: italic; padding-left: 34px; margin-bottom: 2px; }
  .perks ul { padding-left: 52px; }
  .perks li { margin-bottom: 1px; }

  .contact-footer {
    position: absolute;
    left: 0; right: 0; bottom: 0;
    height: 96px;
    background: var(--red);
    color: #fff;
    text-align: center;
    font-weight: 600;
    font-size: 12.5px;
    line-height: 1.45;
    display: flex;
    flex-direction: column;
    justify-content: center;
  }

  /* back side */
  .back-content { padding-top: 40px; }
  .intro { margin-top: 10px; }
  .activity-grid {
    display: grid;
    grid-template-columns: 1fr 1fr;
    gap: 6px;
    padding: 14px 12px 0 12px;
  }
  .activity {
    position: relative;
    height: 120px;
    overflow: hidden;
  }
  .activity__photo { position: absolute; inset: 0; }
  .activity__label {
    position: absolute;
    left: 0; right: 0; bottom: 0;
    background: var(--red);
    color: #fff;
    font-weight: 700;
    font-size: 13px;
    text-align: center;
    padding: 5px 0;
  }
  .photo--reef { background: linear-gradient(170deg, #9fdde0, #4aa9b4 60%, #cfe6d8); }
  .photo--glider { background: linear-gradient(160deg, #2a8fb6, #0f5675); }
  .photo--cliff { background: linear-gradient(180deg, #b8dcef 0%, #2f9cc4 55%, #8a5a3c 100%); }
  .photo--fishing { background: linear-gradient(170deg, #38a9c2, #1a6b86 70%, #6a8c68); }
  .photo--paddle { background: linear-gradient(180deg, #c7dbe6, #4a8ab0 60%, #2e6b8e); }
  .photo--beach { background: linear-gradient(180deg, #cfe2ec, #f1ece4 50%, var(--sand)); }

  .outro { margin-top: 14px; }
  .cta-box {
    margin: 14px 40px 0;
    border: 2px dotted var(--red);
    color: var(--red);
    font-weight: 700;
    font-size: 15px;
    text-align: center;
    padding: 10px 8px;
    line-height: 1.3;
  }
</style>
</head>
<body>

<article class="flyer flyer--front">
  <header class="brand">
    <span class="brand__mark"></span>
    <span class="brand__name">Driftwood Bay</span>
  </header>

  <div class="photo-hero" role="img" aria-label="Family standing on the bow of a sailing yacht near a green shoreline"></div>

  <h1 class="headline-band">Experience yacht charter<br>service at its finest!</h1>

  <section class="front-content">
    <div class="body-copy">
      <p>Sail away with us on a Luxury Charter experience complete with a full brunch spread. During our sail we will take you to the hottest destination spots in the Caribbean surrounding St Thomas and St John.</p>
      <p>Warm, fresh baked afternoon cookies will be served on the way back from our days journeys. Unlimited water, sodas, beer and rum punch will be provided for the entire group to enjoy throughout the day.</p>
    </div>

    <div class="galley">
      <h2 class="section-tab">Gilded Galley</h2>
      <div class="body-copy">
        <p>Driftwood Bay is now one of the only chartering companies that offer a private full day brunch sail.</p>
      </div>
      <div class="perks">
        <p class="perks__lead">All Guests will receive "Harbor Fizz"</p>
        <ul>
          <li>Up to 12 guests</li>
          <li>Full Brunch Spread to include, Assorted fruit tower, Artesian Waffle Board, Frittata's, Loaded Avocado Toast or an All American Breakfast.</li>
          <li>Specialty Cocktails with Bottle Service options available</li>
        </ul>
      </div>
    </div>
  </section>

  <footer class="contact-footer">
    <span>Call us at : (340) 555-0187</span>
    <span>email: Info@driftwoodbayvoyages.example</span>
    <span>www.driftwoodbayvoyages.example</span>
  </footer>
</article>

<article class="flyer flyer--back">
  <section class="back-content">
    <h2 class="section-tab">Our Unique Activities</h2>
    <div class="body-copy intro">
      <p>Driftwood Bay is so glad to announce the beginning of our charters in the US Virgin Islands. We are confident in our charters to bring joy and excitement for your entire group. Embark on an unforgettable adventure with our crew at Driftwood Bay while they cater to your every need. Here's a closer look on what activities we offer while you sail with us :</p>
    </div>

    <div class="activity-grid">
      <figure class="activity">
        <div class="activity__photo photo--reef" role="img" aria-label="Snorkeler swimming above a stingray in clear shallow water"></div>
        <figcaption class="activity__label">Snorkeling</figcaption>
      </figure>
      <figure class="activity">
        <div class="activity__photo photo--glider" role="img" aria-label="Diver with mask exploring deep blue water"></div>
        <figcaption class="activity__label">WaveGliders</figcaption>
      </figure>
      <figure class="activity">
        <div class="activity__photo photo--cliff" role="img" aria-label="Friends jumping from rocky cliffs into the turquoise sea"></div>
        <figcaption class="activity__label">Cliff Jumping</figcaption>
      </figure>
      <figure class="activity">
        <div class="activity__photo photo--fishing" role="img" aria-label="Spear fisher swimming over a coral reef"></div>
        <figcaption class="activity__label">Spear Fishing</figcaption>
      </figure>
      <figure class="activity">
        <div class="activity__photo photo--paddle" role="img" aria-label="Two people on a paddle board in open water"></div>
        <figcaption class="activity__label">Paddle Boarding</figcaption>
      </figure>
      <figure class="activity">
        <div class="activity__photo photo--beach" role="img" aria-label="Child riding a boogie board through breaking surf on the beach"></div>
        <figcaption class="activity__label">Beach Games</figcaption>
      </figure>
    </div>

    <div class="body-copy outro">
      <p>Our "Gilded Galley" is one of the only brunch charters in the USVI. Experience the breathtaking Caribbean Sea while our crew serves you the brunch of your choice.</p>
    </div>

    <p class="cta-box">Come enjoy the water with us!<br>Driftwood Bay!</p>
  </section>

  <footer class="contact-footer">
    <span>Call us at : (340) 555-0187</span>
    <span>email: Info@driftwoodbayvoyages.example</span>
    <span>www.driftwoodbayvoyages.example</span>
  </footer>
</article>

</body>
</html>
```